Blue Harbor polishing
Project: Business cards and stationary
Business cards and stationary - Automotive
Business cards and stationary
Modern
Ray Mercer
Owner
1735 E. Corbin Rd. Prudenville Mi. 48639
raymercer@mailbrook.net
blueharborshine.us
All logos and lettering is "white" with a black glossy background, I would like to look at tow different logos # 308 and 309. One may look better on the business card. I hope they uploaded!
Visit our website @ blueharborshine.us for a list of services and prices. Visit us on facebook @ Blue Harbor shine

```html
<!DOCTYPE html>
<html lang="en">
<head>
<meta charset="utf-8">
<title>Blue Harbor shine — Business Cards</title>
<link rel="stylesheet" href="https://fonts.googleapis.com/css2?family=Roboto:wght@300;400;700;900&display=swap">
<style>
  :root {
    --backdrop: #5c5e60;
    --card-black: #0b0b0c;
    --card-sheen: #2a2a2d;
    --ink-white: #ffffff;
    --ink-silver: #c9cbcf;
  }
  html, body {
    margin: 0;
    padding: 0;
    width: 1200px;
    height: 901px;
    overflow: hidden;
    background: var(--backdrop);
    font-family: "Roboto", Arial, sans-serif;
  }
  .stage {
    width: 1200px;
    height: 901px;
    display: flex;
    align-items: center;
    justify-content: center;
    gap: 60px;
  }
  .card {
    position: relative;
    width: 525px;
    height: 300px;
    border-radius: 4px;
    background:
      linear-gradient(125deg, transparent 0 55%, rgba(255,255,255,0.07) 55% 70%, transparent 70%),
      linear-gradient(160deg, var(--card-sheen) 0%, var(--card-black) 45%, var(--card-black) 100%);
    box-shadow: 0 18px 40px rgba(0,0,0,0.45);
    overflow: hidden;
    color: var(--ink-white);
  }
  .card-front .brand {
    position: absolute;
    left: 70px;
    top: 78px;
    display: flex;
    align-items: center;
    gap: 14px;
  }
  .brand-dot {
    width: 26px;
    height: 26px;
    border-radius: 50%;
    background: var(--ink-silver);
  }
  .brand-name {
    font-weight: 900;
    font-size: 38px;
    letter-spacing: 0.5px;
    color: var(--ink-white);
    white-space: nowrap;
  }
  .card-front .identity {
    position: absolute;
    left: 70px;
    top: 180px;
    margin: 0;
    font-size: 24px;
    color: var(--ink-white);
  }
  .identity .person { font-weight: 700; }
  .identity .divider { font-weight: 300; margin: 0 8px; color: var(--ink-silver); }
  .identity .role { font-weight: 300; }

  .card-back .contact {
    position: absolute;
    right: 40px;
    top: 44px;
    list-style: none;
    margin: 0;
    padding: 0;
    font-size: 15px;
    font-weight: 400;
    color: var(--ink-silver);
    line-height: 1.9;
    white-space: nowrap;
  }
  .contact li { display: flex; align-items: center; gap: 8px; }
  .contact svg { width: 13px; height: 13px; fill: var(--ink-silver); flex: none; }
  .contact .address { color: var(--ink-white); font-weight: 700; }
</style>
</head>
<body>
<main class="stage">
  <section class="card card-front" aria-label="Business card front">
    <div class="brand">
      <span class="brand-dot"></span>
      <span class="brand-name">Blue Harbor shine</span>
    </div>
    <p class="identity">
      <span class="person">Ray Mercer</span><span class="divider">/</span><span class="role">Owner</span>
    </p>
  </section>

  <section class="card card-back" aria-label="Business card back">
    <ul class="contact">
      <li class="address">1735 E. Corbin Rd. Larkmoor Mi. 40217</li>
      <li>
        <svg viewBox="0 0 24 24" aria-hidden="true"><path d="M6.6 10.8a15.1 15.1 0 0 0 6.6 6.6l2.2-2.2a1 1 0 0 1 1-.25 11.4 11.4 0 0 0 3.6.6 1 1 0 0 1 1 1V20a1 1 0 0 1-1 1A17 17 0 0 1 3 4a1 1 0 0 1 1-1h3.5a1 1 0 0 1 1 1c0 1.25.2 2.45.6 3.6a1 1 0 0 1-.25 1z"/></svg>
        (555) 014-2286
      </li>
      <li>
        <svg viewBox="0 0 24 24" aria-hidden="true"><path d="M2 5h20v14H2zm2 2v.5l8 5 8-5V7z"/></svg>
        raymercer@mailbrook.net
      </li>
      <li>
        <svg viewBox="0 0 24 24" aria-hidden="true"><circle cx="12" cy="12" r="9" fill="none" stroke="#c9cbcf" stroke-width="2"/><path d="M3 12h18M12 3c3 3 3 15 0 18M12 3c-3 3-3 15 0 18" fill="none" stroke="#c9cbcf" stroke-width="1.6"/></svg>
        blueharborshine.us
      </li>
    </ul>
  </section>
</main>
</body>
</html>
```